Dodgeball League website

I require a nice, cool and attractive website for a new dodgeball league competition. I will need in PSD:

- Home Page
- Generic pages for news, about us etc
- Rank page with a table of team scores. stats etc

*Please design this with a Joomla*

I have attached:
- a logo
- site map for the links
- page layout guide

Example site for layout
http://www.velmorcircuit.com/

Design
Retro,cool feel, matches well with logo

Contact me if you have any questions

Reason: Would like to see a few more designs

Target Market(s)

Young adults 18 - 35.

Industry/Entity Type

News

Colors

Designer to choose colors to be used in the design.

Requirements
Must have
• I want a cool, retro feel to the website. Not to picky on the colors. Something that will match nicely with the logo given. I will give feedback on it.
Calm colors not too bright and overwhelming
Nice to have
• Include some pictures within the picture slider so I can get a feel for the website.
Nice clean background
Should not have
• To much clutter of text
Do not put pictures in the background.

```html
<!DOCTYPE html>
<html lang="en">
<head>
<meta charset="utf-8">
<title>Harbour Dodge League</title>
<link href="https://fonts.googleapis.com/css2?family=Open+Sans:wght@400;600;700&family=Noto+Serif:wght@400&display=swap" rel="stylesheet">
<style>
:root{
  --orange:#d9572a;
  --orange-light:#e9743f;
  --orange-dark:#b9441c;
  --text:#4a4a4a;
  --muted:#666;
  --panel:#f2f2f2;
  --line:#dcdcdc;
  --footer:#454545;
  --navy:#1f4a9a;
  --sky:#3b8fd6;
}
*{box-sizing:border-box;margin:0;padding:0}
html,body{width:742px;height:1200px;overflow:hidden}
body{position:relative;background:#fff;font-family:"Open Sans",Arial,sans-serif;color:var(--text);font-size:8px}
.abs{position:absolute}
a{color:inherit;text-decoration:none}

/* header */
.header{left:0;top:0;width:742px;height:98px;background:linear-gradient(180deg,#fff 0%,#f1f1f1 100%)}
.brand{left:74px;top:14px;display:flex;align-items:center;gap:6px;color:var(--orange);font-weight:700;font-size:12px;line-height:1.1;width:110px}
.brand-dot{width:22px;height:22px;border-radius:50%;background:var(--orange);flex:none}
.toplinks{right:66px;top:11px;font-size:6.5px;color:var(--orange);font-weight:600;display:flex;gap:5px}
.toplinks span.sep{color:#999}
.scoreboard{left:528px;top:34px;width:146px;height:32px;background:#111;border:2px solid #c24a1f;padding:5px 6px;color:#fff;font-size:5.5px}
.scoreboard .row{display:flex;justify-content:space-between;height:10px;align-items:center;border-bottom:1px solid #333}
.scoreboard .pts{display:flex;gap:8px}
.nav{left:64px;top:84px;width:616px;height:28px;border-radius:6px;background:linear-gradient(180deg,var(--orange-light),var(--orange-dark));display:flex;align-items:center;justify-content:space-around;color:#fff;font-weight:700;font-size:7.5px;z-index:2;box-shadow:0 2px 3px rgba(0,0,0,.3)}
.hero{left:0;top:98px;width:742px;height:302px;background:linear-gradient(180deg,#8a7a6a 0%,#b58550 55%,#c98a48 100%)}

/* news */
.section-title{font-size:13px;font-weight:700;color:var(--orange-dark)}
.section-title span{color:var(--text);font-weight:600}
.news-item{left:67px;width:400px}
.thumb{position:absolute;left:0;top:0;width:70px;height:72px;background:linear-gradient(135deg,#8a6a50,#3a4a8a)}
.news-item h3{position:absolute;left:78px;top:2px;font-size:9px;color:var(--orange);font-weight:600}
.news-item p{position:absolute;left:78px;top:18px;width:300px;font-size:7.2px;line-height:11px;color:var(--text)}
.news-item p a{color:var(--orange)}
.divider{left:67px;top:518px;width:400px;height:1px;background:var(--line)}

/* right column */
.like-banner{left:482px;top:410px;width:192px;height:53px;background:linear-gradient(180deg,var(--sky),var(--navy));color:#fff;display:flex;align-items:center;justify-content:center;gap:10px;font-size:20px;font-weight:700}
.like-banner small{display:block;font-size:10px;font-weight:600}
.like-sq{width:30px;height:30px;background:#fff;border-radius:4px}
.message{left:478px;top:486px;width:200px;height:68px;background:#eee;border-radius:5px;padding:5px}
.message-inner{position:relative;width:100%;height:100%;border-radius:4px;background:linear-gradient(180deg,#5fb4e6,#2a7fc4);overflow:hidden}
.message-inner .t1{position:absolute;left:42px;top:9px;color:#e8452a;font-weight:700;font-size:9px;font-style:italic}
.message-inner .t2{position:absolute;left:42px;top:18px;color:#fff;font-size:15px;letter-spacing:1px}
.message-inner .btn{position:absolute;left:8px;top:40px;background:#fff;color:var(--orange);font-weight:700;font-size:6.5px;padding:2px 8px;border-radius:6px;letter-spacing:.5px}
.message-art{position:absolute;right:10px;top:4px;width:50px;height:50px;border-radius:6px;background:linear-gradient(135deg,#f4b040,#4a6a8a)}
.likebox{left:478px;top:576px;width:196px;height:134px;border:1px solid var(--line);background:#fff;padding:6px}
.likebox .head{display:flex;gap:6px}
.likebox .page-sq{width:28px;height:28px;background:var(--orange)}
.likebox .name{font-size:7px;font-weight:700;color:var(--navy)}
.likebox .btn{margin-top:3px;border:1px solid #ccc;font-size:5.5px;padding:1px 4px;color:var(--navy);display:inline-block}
.likebox .count{margin-top:7px;font-size:5.5px;color:#555}
.fans{margin-top:4px;height:52px;background:linear-gradient(90deg,#c9b8a8,#9aa8c0)}
.likebox .plugin{margin-top:6px;font-size:5px;color:#777}
.map{left:482px;top:720px;width:192px;height:116px;border:1px solid var(--line);background:linear-gradient(135deg,#e8e4d8,#cfe0ee 60%,#b8d4ec)}

/* league table */
.tabs{left:77px;top:625px;display:flex;align-items:flex-end}
.tab-active{width:159px;height:23px;background:linear-gradient(180deg,var(--orange-light),var(--orange-dark));color:#fff;font-weight:700;font-size:11px;padding:4px 8px;border-radius:4px 4px 0 0}
.tab{font-size:11.5px;font-weight:600;color:#333;padding:4px 12px}
.table{left:69px;top:648px;width:401px;height:187px;border:1px solid var(--line);border-radius:4px;background:#fafafa}
.col{position:absolute;top:6px;width:185px}
.col.left{left:6px}
.col.right{left:212px}
.table .vline{position:absolute;left:199px;top:8px;width:1px;height:170px;background:var(--line)}
.rank{position:relative;height:38px;border-bottom:1px dotted var(--line)}
.rank .num{position:absolute;left:1px;top:9px;font-size:8px;color:var(--orange)}
.rank .name{position:absolute;left:18px;top:8px;font-size:6.5px;color:var(--orange);font-weight:600}
.rank .name::before{content:"";display:inline-block;border-left:3px solid var(--orange);border-top:2.5px solid transparent;border-bottom:2.5px solid transparent;margin-right:4px}
.rank .desc{position:absolute;left:18px;top:19px;font-size:6.5px;color:#333}
.rank .score{position:absolute;right:0;top:13px;font-size:7px;color:var(--orange);font-weight:600}

/* top 3 */
.top-card{top:872px;width:188px;height:114px;border-radius:8px;background:linear-gradient(180deg,#fff,#f1f1f1);box-shadow:0 3px 4px rgba(0,0,0,.08)}
.top-card h4{position:absolute;left:9px;top:8px;font-family:"Noto Serif",Georgia,serif;font-weight:400;font-size:13px;color:#333}
.top-card ol{position:absolute;left:9px;top:32px;list-style:none;font-size:6.8px;line-height:15px;color:#555}
.top-card .more{position:absolute;left:9px;top:88px;background:linear-gradient(180deg,var(--orange-light),var(--orange-dark));color:#fff;font-size:7px;font-weight:600;padding:3px 8px;border-radius:4px}
.top-photo{position:absolute;right:-4px;top:-12px;width:74px;height:74px;border-radius:50%;border:3px solid #fff;box-shadow:0 1px 4px rgba(0,0,0,.3);background:linear-gradient(135deg,#9ab0c8,#c8a890)}

/* sponsors */
.sponsor-tab{left:312px;top:1022px;width:116px;height:24px;background:linear-gradient(180deg,var(--orange-light),var(--orange-dark));color:#fff;font-weight:700;font-size:11px;text-align:center;line-height:24px;border-radius:4px 4px 0 0}
.sponsors{left:66px;top:1046px;width:608px;height:60px;background:var(--panel);border-radius:5px;display:flex;align-items:center;justify-content:space-around;padding:0 14px;color:#8a8a8a;font-size:13px}
.sponsor{display:flex;align-items:center;gap:3px}
.sponsor i{width:12px;height:12px;background:#9a9a9a;display:block}

/* footer */
.footer{left:0;top:1122px;width:742px;height:78px;background:var(--footer);color:#fff}
.footer-links{position:absolute;left:63px;top:20px;font-size:7px;display:flex;gap:10px}
.footer-links .sep{color:#ccc}
.footer p{position:absolute;left:63px;font-size:7px}
.footer-brand{position:absolute;left:606px;top:22px;display:flex;align-items:center;gap:4px;color:var(--orange-light);font-weight:700;font-size:8px;width:80px;line-height:1.1}
.footer-brand i{width:14px;height:14px;border-radius:50%;background:var(--orange-light);display:block;flex:none}
</style>
</head>
<body>

<header class="abs header"></header>
<div class="abs brand"><span class="brand-dot"></span><span>Harbour Dodge League</span></div>
<nav class="abs toplinks">
  <a>Live Scoreboard</a><span class="sep">|</span><a>Results</a><span class="sep">|</span><a>Draws &amp; Schedule</a><span class="sep">|</span><a>TV Watch</a><span class="sep">|</span><a>Live</a><span class="sep">|</span><a>Fantasy</a><span class="sep">|</span><a>Mobile</a>
</nav>
<div class="abs scoreboard">
  <div class="row"><span>Tomas Reiner</span><span class="pts"><span>0</span><span>7</span><span>0</span></span></div>
  <div class="row"><span>• Ivo Daskalov</span><span class="pts"><span>0</span><span>6</span><span>0</span></span></div>
</div>
<nav class="abs nav">
  <a>HOME</a><a>ABOUT</a><a>TEAMS</a><a>SCHEDULE</a><a>NEWS</a><a>PHOTOS &amp; VIDEOS</a><a>REGISTER</a><a>CONTACT US</a>
</nav>
<div class="abs hero" role="img" aria-label="Slider photo of a dodgeball match on an indoor wooden court"></div>

<h2 class="abs section-title" style="left:64px;top:407px">Recent <span>News</span></h2>
<article class="abs news-item" style="top:432px;height:80px">
  <div class="thumb" role="img" aria-label="Portrait of a league player"></div>
  <h3>Get off your butt and exercise, orders your doc</h3>
  <p>simply dummy text of the printing and typesetting industry. Lorem Ipsum has been the industry's standard dummy text ever since the 1500s, when an unknown printer took a galley of type and scrambled it to make a type specimen book. It has survived not only five centuries, since the 1500s, when an unknown printer took a galley of type galley of type and scrambled it to make...<a>[Readmore..]</a></p>
</article>
<div class="abs divider"></div>
<article class="abs news-item" style="top:527px;height:72px">
  <div class="thumb" role="img" aria-label="Player in a purple team uniform"></div>
  <h3>Get off your butt and exercise, orders your doc</h3>
  <p>simply dummy text of the printing and typesetting industry. Lorem Ipsum has been the industry's standard dummy text ever since the 1500s, when an unknown printer took a galley of type and scrambled it to make a type specimen book. It has survived not only five centuries, scrambled it to make...<a>[Readmore..]</a></p>
</article>

<aside class="abs like-banner"><div><small>Like us on</small>Sidewall</div><span class="like-sq"></span></aside>
<aside class="abs message">
  <div class="message-inner">
    <span class="t1">SEND A</span>
    <span class="t2">MESSAGE</span>
    <span class="btn">CLICK HERE</span>
    <div class="message-art" role="img" aria-label="Illustration of a mailbox with letters"></div>
  </div>
</aside>
<aside class="abs likebox">
  <div class="head"><span class="page-sq"></span><div><div class="name">Northgate</div><span class="btn">Like</span></div></div>
  <div class="count">29 190 people like Northgate.</div>
  <div class="fans" role="img" aria-label="Grid of fan profile pictures"></div>
  <div class="plugin">Social plugin</div>
</aside>
<div class="abs map" role="img" aria-label="Street map of the league venue area"></div>

<div class="abs tabs"><div class="tab-active">Ultimate Rubber League</div><div class="tab">Ultimate Foam League</div></div>
<section class="abs table">
  <div class="col left">
    <div class="rank"><span class="num">1.</span><span class="name">Dario Velken</span><span class="desc">Set to make sixth appearance</span><span class="score">11,670</span></div>
    <div class="rank"><span class="num">2.</span><span class="name">Dario Velken</span><span class="desc">Set to make sixth appearance</span><span class="score">11,670</span></div>
    <div class="rank"><span class="num">3.</span><span class="name">Dario Velken</span><span class="desc">Set to make sixth appearance</span><span class="score">11,670</span></div>
    <div class="rank" style="height:44px"><span class="num" style="top:14px">4.</span><span class="name" style="top:13px">Dario Velken</span><span class="desc" style="top:24px">Set to make sixth appearance</span><span class="score" style="top:18px">11,670</span></div>
  </div>
  <div class="vline"></div>
  <div class="col right">
    <div class="rank"><span class="num">5.</span><span class="name">Dario Velken</span><span class="desc">Set to make sixth appearance</span><span class="score">11,670</span></div>
    <div class="rank"><span class="num">6.</span><span class="name">Dario Velken</span><span class="desc">Set to make sixth appearance</span><span class="score">11,670</span></div>
    <div class="rank"><span class="num">7.</span><span class="name">Dario Velken</span><span class="desc">Set to make sixth appearance</span><span class="score">11,670</span></div>
    <div class="rank" style="height:44px"><span class="num" style="top:14px">8.</span><span class="name" style="top:13px">Dario Velken</span><span class="desc" style="top:24px">Set to make sixth appearance</span><span class="score" style="top:18px">11,670</span></div>
  </div>
</section>

<section class="abs top-card" style="left:70px">
  <h4>Top 3 Killer</h4>
  <ol><li>1. simply dummy text</li><li>2.of the printing and typesetting</li><li>3.Lorem Ipsum has been the</li></ol>
  <a class="more">Learnmore</a>
  <div class="top-photo" role="img" aria-label="Photo of the top killer"></div>
</section>
<section class="abs top-card" style="left:276px">
  <h4>Top 3 Catcher</h4>
  <ol><li>1. simply dummy text</li><li>2.of the printing and typesetting</li><li>3.Lorem Ipsum has been the</li></ol>
  <a class="more">Learnmore</a>
  <div class="top-photo" role="img" aria-label="Photo of the top catcher"></div>
</section>
<section class="abs top-card" style="left:482px">
  <h4>Top 3 Dodger</h4>
  <ol><li>1. simply dummy text</li><li>2.of the printing and typesetting</li><li>3.Lorem Ipsum has been the</li></ol>
  <a class="more">Learnmore</a>
  <div class="top-photo" role="img" aria-label="Photo of the top dodger"></div>
</section>

<div class="abs sponsor-tab">Our Sponsers</div>
<section class="abs sponsors">
  <span class="sponsor"><i></i>brightmill</span>
  <span class="sponsor"><i></i>soundcrate</span>
  <span class="sponsor"><i></i>pixelford</span>
  <span class="sponsor"><i></i>scriptvale</span>
  <span class="sponsor"><i></i>meshbay</span>
  <span class="sponsor"><i></i>clipnest</span>
</section>

<footer class="abs footer">
  <nav class="footer-links">
    <a>Home</a><span class="sep">|</span><a>About</a><span class="sep">|</span><a>Teams</a><span class="sep">|</span><a>Schedule</a><span class="sep">|</span><a>News</a><span class="sep">|</span><a>Photos &amp; Videos</a><span class="sep">|</span><a>Register</a><span class="sep">|</span><a>Contact Us</a>
  </nav>
  <p style="top:36px">Copyright © 2007 - 2013 - Dodgeball League. - All Rights Reserved</p>
  <p style="top:48px">Powered by: harbourdodge.com and CrestlineBids.com</p>
  <div class="footer-brand"><i></i><span>Harbour Dodge League</span></div>
</footer>

</body>
</html>
```